Refresh of Business Card Design

Want to refresh the business card design with the new logo while adhering to style guide as attached. Would like to match feel of website www.durmackvinex.com

```html
<!DOCTYPE html>
<html lang="en">
<head>
<meta charset="utf-8">
<title>Durmack Vinex — Business Card</title>
<link href="https://fonts.googleapis.com/css2?family=Lato:wght@400;700;900&display=swap" rel="stylesheet">
<style>
  :root {
    --page: #2a2a2a;
    --card-black: #111112;
    --card-black-2: #1b1b1d;
    --brand-pink: #e4285a;
    --brand-red: #d8203f;
    --silver: #c9c9cc;
    --white: #ffffff;
  }
  * { box-sizing: border-box; margin: 0; padding: 0; }
  html, body { width: 1200px; height: 939px; overflow: hidden; }
  body {
    background: var(--page);
    font-family: "Lato", sans-serif;
    color: var(--white);
    position: relative;
  }
  .card {
    position: absolute;
    left: 290px;
    width: 620px;
    height: 354px;
    border-radius: 18px;
    overflow: hidden;
    background: linear-gradient(160deg, var(--card-black-2), var(--card-black));
    box-shadow: 0 14px 30px rgba(0,0,0,.55);
  }

  /* Front */
  .card--front { top: 70px; }
  .front-glow {
    position: absolute;
    inset: 0;
    background: radial-gradient(ellipse 260px 200px at 32% 48%, rgba(228,40,90,.85), rgba(150,15,45,.4) 45%, rgba(17,17,18,0) 80%);
  }
  .front-brand {
    position: absolute;
    left: 50%;
    top: 130px;
    transform: translateX(-50%);
    display: flex;
    align-items: center;
    gap: 16px;
  }
  .brand-dot {
    width: 58px; height: 58px;
    border-radius: 50%;
    background: var(--brand-red);
    border: 4px solid var(--silver);
  }
  .brand-name {
    font-weight: 900;
    font-size: 34px;
    letter-spacing: 2px;
    text-transform: uppercase;
    white-space: nowrap;
  }
  .front-url {
    position: absolute;
    left: 0; right: 0;
    bottom: 42px;
    text-align: center;
    font-size: 16px;
    letter-spacing: 2px;
    text-transform: uppercase;
  }
  .front-url b { font-weight: 700; }

  /* Back */
  .card--back { top: 500px; }
  .info-band {
    position: absolute;
    left: 0; right: 0;
    top: 70px;
    height: 208px;
    background: var(--brand-pink);
    border-top: 5px solid var(--silver);
    border-bottom: 5px solid var(--silver);
    box-shadow: 0 -6px 0 var(--card-black), 0 6px 0 var(--card-black);
  }
  .back-brand {
    position: absolute;
    left: 28px; top: 112px;
    width: 210px;
    height: 130px;
    border-radius: 14px;
    background: var(--card-black);
    border: 4px solid var(--silver);
    display: flex;
    flex-direction: column;
    align-items: center;
    justify-content: center;
    gap: 10px;
  }
  .back-brand .brand-dot { width: 44px; height: 44px; border-width: 3px; }
  .back-brand .brand-name { font-size: 20px; letter-spacing: 1.5px; }
  .contact {
    position: absolute;
    left: 270px; top: 92px;
  }
  .contact-name {
    font-weight: 900;
    font-size: 30px;
    letter-spacing: .5px;
    text-transform: uppercase;
  }
  .contact-role { font-size: 18px; margin: 0 0 10px 2px; }
  .contact-list { list-style: none; }
  .contact-list li {
    display: flex;
    align-items: center;
    gap: 10px;
    font-size: 15px;
    line-height: 22px;
  }
  .contact-list svg { width: 13px; height: 13px; fill: var(--white); flex: none; }
</style>
</head>
<body>

<section class="card card--front" aria-label="Card front">
  <div class="front-glow" role="img" aria-label="Soft red glow decoration"></div>
  <div class="front-brand">
    <span class="brand-dot"></span>
    <span class="brand-name">Durmack Vinex</span>
  </div>
  <p class="front-url">www.<b>durmackvinex</b>.com</p>
</section>

<section class="card card--back" aria-label="Card back">
  <div class="info-band"></div>
  <div class="back-brand">
    <span class="brand-dot"></span>
    <span class="brand-name">Durmack Vinex</span>
  </div>
  <div class="contact">
    <h1 class="contact-name">Reid Halloway</h1>
    <p class="contact-role">Sales</p>
    <ul class="contact-list">
      <li><svg viewBox="0 0 12 12"><path d="M3 0h6a1 1 0 0 1 1 1v10a1 1 0 0 1-1 1H3a1 1 0 0 1-1-1V1a1 1 0 0 1 1-1zm0 2v7h6V2z"/></svg>555.014.2290</li>
      <li><svg viewBox="0 0 12 12"><path d="M0 2h12v8H0zm1 1v.4l5 3.2 5-3.2V3z"/></svg>rhalloway@durmackvinex.com</li>
      <li><svg viewBox="0 0 12 12"><circle cx="6" cy="6" r="6"/></svg>www.durmackvinex.com</li>
      <li><svg viewBox="0 0 12 12"><path d="M6 0a4 4 0 0 1 4 4c0 3-4 8-4 8S2 7 2 4a4 4 0 0 1 4-4zm0 2.5a1.5 1.5 0 1 0 0 3 1.5 1.5 0 0 0 0-3z"/></svg>42 Linden Ave Marlow, TX 70104</li>
      <li><svg viewBox="0 0 12 12"><path d="M6 0a4 4 0 0 1 4 4c0 3-4 8-4 8S2 7 2 4a4 4 0 0 1 4-4zm0 2.5a1.5 1.5 0 1 0 0 3 1.5 1.5 0 0 0 0-3z"/></svg>P.O.Box 30418 Easton, TX 70012</li>
    </ul>
  </div>
</section>

</body>
</html>
```